Harbortail Keepers Florida Retractable Banner Design

Looking for a fresh, modern, eye catching yet informative retractable banner design for our vendor booth events.

Our color scheme is teal, dark yellow, black, and white

Would like to include our services of Overnights, Pop in Visits, Dog Walking, Transport, and Attendants. We are veterinary professionals that offer a higher tier level of pet care.

Our tagline is Raising the Bar in Harbortail Animal Care

Require logo to be incorporated

Would like our images used or included

Would like to include that we offer law enforcement and military discounts

www.harbortailkeepers.net is our website
An example of our print marketing materials attached

```html
<!DOCTYPE html>
<html lang="en">
<head>
<meta charset="utf-8">
<title>Harbortail Keepers Florida – Retractable Banner</title>
<link href="https://fonts.googleapis.com/css2?family=Allura&family=Montserrat:wght@500;600;700&display=swap" rel="stylesheet">
<style>
  :root {
    --teal: #3cc8c6;
    --gold: #f2b705;
    --black: #060606;
    --white: #ffffff;
    --page: #ffffff;
    --fur-light: #b9b6b1;
    --fur-dark: #5e5b57;
  }
  * { margin: 0; padding: 0; box-sizing: border-box; }
  html, body {
    width: 1200px; height: 841px; overflow: hidden;
    background: var(--page);
    font-family: "Montserrat", Arial, sans-serif;
  }
  .banner {
    position: absolute; left: 435px; top: 10px;
    width: 330px; height: 822px;
    background: var(--white);
    overflow: hidden;
  }
  .banner__dark {
    position: absolute; left: 0; top: 277px; width: 100%; bottom: 0;
    background: var(--black);
  }
  .brand {
    position: absolute; left: 0; top: 48px; width: 100%;
    text-align: center;
  }
  .brand__mark {
    display: block; width: 40px; height: 40px; margin: 0 auto 8px;
    border-radius: 50%; background: var(--teal);
  }
  .brand__name {
    font-weight: 700; font-size: 16px; color: var(--gold);
    letter-spacing: 0.2px; text-transform: uppercase;
  }
  .brand__services {
    margin-top: 2px; font-weight: 700; font-size: 5.5px;
    letter-spacing: 0.9px; color: var(--teal);
  }
  .photo-cat {
    position: absolute; left: 101px; top: 128px;
    width: 137px; height: 185px;
    border-radius: 48% 48% 30% 30% / 40% 40% 18% 18%;
    background: radial-gradient(ellipse at 50% 35%, var(--fur-light), #8a8782 60%, var(--fur-dark));
  }
  .photo-dog {
    position: absolute; left: 4px; top: 666px;
    width: 225px; height: 156px;
    border-radius: 60% 50% 0 0 / 70% 60% 0 0;
    background: radial-gradient(ellipse at 55% 50%, #d5d5d5, #8b8b8b 45%, #2b2b2b 80%, var(--black));
  }
  .rule-v {
    position: absolute; left: 46px; top: 345px;
    width: 2px; height: 171px; background: var(--teal);
  }
  .rule-h {
    position: absolute; left: 33px; top: 412px;
    width: 265px; height: 2px; background: var(--teal);
  }
  .headline-script {
    position: absolute; left: 52px; top: 322px;
    font-family: "Allura", cursive;
    font-size: 50px; line-height: 1; color: var(--teal);
    white-space: nowrap;
  }
  .headline-caps {
    position: absolute; left: 54px; top: 386px;
    font-weight: 600; font-size: 15.5px; color: var(--gold);
    white-space: nowrap;
  }
  .intro {
    position: absolute; left: 55px; top: 425px; width: 250px;
    font-weight: 500; font-size: 11.2px; line-height: 14.5px; color: var(--white);
  }
  .intro strong { color: var(--gold); font-weight: 600; }
  .offer {
    position: absolute; left: 0; top: 532px; width: 100%;
    text-align: center; color: var(--white);
  }
  .offer__title {
    font-weight: 700; font-size: 15.5px; color: var(--teal); line-height: 18px;
  }
  .offer__text { font-weight: 500; font-size: 12.4px; line-height: 16px; }
  .website {
    position: absolute; left: 0; top: 628px; width: 100%;
    text-align: center; font-weight: 500; font-size: 11.5px;
    letter-spacing: 1px; color: var(--white);
  }
  .website span { color: var(--teal); }
</style>
</head>
<body>
  <main class="banner">
    <div class="banner__dark"></div>

    <header class="brand">
      <span class="brand__mark"></span>
      <div class="brand__name">Harbortail Keepers</div>
      <div class="brand__services">OVERNIGHTS · POP IN VISITS · DOG WALKING</div>
    </header>

    <div class="photo-cat" role="img" aria-label="Photo of a grey tabby cat resting its paws over the dark panel"></div>

    <div class="rule-v"></div>
    <div class="rule-h"></div>
    <h1 class="headline-script">Raising the Bar</h1>
    <h2 class="headline-caps">IN HARBORTAIL ANIMAL CARE</h2>

    <p class="intro">We are a <strong>Licensed, Bonded + Insured</strong> Pet care company that offers overnights, pop in visits, dog walking, cat sitting + more in the comfort of your own home.</p>

    <section class="offer">
      <div class="offer__title">WE OFFER</div>
      <div class="offer__text">Law enforcement and military<br>discounts</div>
    </section>

    <p class="website">www.<span>harbortailkeepers</span>.net</p>

    <div class="photo-dog" role="img" aria-label="Photo of a merle shepherd dog looking upward on a black background"></div>
  </main>
</body>
</html>
```